Australia's newest tech recruitment startup

We are a new tech startup in the recruitment space.

We leverage the existing infrastructure of the recruitment network and bundle a value market based business model (like pixel flock) that appeals to business.

We are very individual, afraid of no one, minimalist, and defiantly NO "BS"!!

We're not cut price think Vellmar Auste rather than Korvani
Updates

Hey Everyone,

thanks so much for your designs. I have eliminated a lot of designs but if I havent to yours then your in with a shot. I would like to see the designs updated with a spot for our twitter handle, my blog address & our linkedIn group address. 

For some designs I think some of the above would look ok on the back of the card so not to make the front look too messy. 

thanks   

Target Market(s)

Our target market is SME's young baby boomer and Gen X

Industry/Entity Type

Business

Requirements
Must have
• Company logo, doesn't have to be both

```html
<!DOCTYPE html>
<html lang="en">
<head>
<meta charset="utf-8">
<title>Kestrel Hire – Business Card</title>
<link href="https://fonts.googleapis.com/css2?family=Arimo:wght@400;700&display=swap" rel="stylesheet">
<style>
  :root {
    --brand-blue: #00b1e9;
    --paper: #ffffff;
    --rule-grey: #d9dadc;
    --backdrop: #e6e7ec;
    --ink-white: #ffffff;
  }
  html, body {
    margin: 0;
    width: 1200px;
    height: 987px;
    overflow: hidden;
    background: var(--backdrop);
    font-family: "Arimo", Arial, sans-serif;
  }
  .canvas {
    width: 1200px;
    height: 987px;
    display: flex;
    align-items: center;
    justify-content: center;
    gap: 44px;
  }
  .card {
    position: relative;
    width: 540px;
    height: 310px;
    border-radius: 24px;
    overflow: hidden;
    box-shadow: 0 6px 18px rgba(0, 0, 0, 0.18);
  }
  .card-backdrop {
    position: absolute;
    inset: 0;
    width: 100%;
    height: 100%;
  }
  .brand-name {
    position: absolute;
    margin: 0;
    font-weight: 700;
    letter-spacing: -0.5px;
    white-space: nowrap;
  }
  /* Front */
  .card-front .brand-name {
    top: 58px;
    left: 150px;
    font-size: 50px;
    color: var(--brand-blue);
  }
  .holder {
    position: absolute;
    left: 34px;
    top: 200px;
    color: var(--ink-white);
    text-align: right;
    width: 118px;
  }
  .holder-name {
    margin: 0;
    font-size: 19px;
    font-weight: 700;
  }
  .holder-title {
    margin: 2px 0 0;
    font-size: 15px;
  }
  .divider {
    position: absolute;
    left: 168px;
    top: 200px;
    width: 1px;
    height: 88px;
    background: var(--ink-white);
    opacity: 0.8;
  }
  .contact-list {
    position: absolute;
    left: 184px;
    top: 214px;
    margin: 0;
    padding: 0;
    list-style: none;
    color: var(--ink-white);
    font-size: 14px;
    line-height: 23px;
  }
  .contact-list li {
    display: flex;
    align-items: center;
    gap: 7px;
  }
  .contact-icon {
    width: 12px;
    height: 12px;
    flex: none;
  }
  /* Back */
  .card-back { background: var(--brand-blue); }
  .card-back .brand-name {
    top: 50%;
    left: 50%;
    transform: translate(-50%, -50%);
    font-size: 60px;
    color: var(--ink-white);
  }
</style>
</head>
<body>
<main class="canvas">
  <section class="card card-front" aria-label="Card front">
    <svg class="card-backdrop" viewBox="0 0 540 310" preserveAspectRatio="none" aria-hidden="true">
      <rect width="540" height="310" fill="var(--paper)"/>
      <path d="M0 100 C 170 150, 370 215, 540 242 L540 310 L0 310 Z" fill="var(--rule-grey)"/>
      <path d="M0 112 C 170 162, 370 228, 540 254 L540 310 L0 310 Z" fill="var(--brand-blue)"/>
    </svg>
    <h1 class="brand-name">Kestrel Hire</h1>
    <div class="holder">
      <p class="holder-name">Your Name</p>
      <p class="holder-title">Title</p>
    </div>
    <div class="divider"></div>
    <ul class="contact-list">
      <li>
        <svg class="contact-icon" viewBox="0 0 12 12" aria-hidden="true"><circle cx="6" cy="6" r="5.5" fill="none" stroke="#fff"/><path d="M4 3.2 L5 5 L4.4 5.6 Q5.2 7 6.4 7.6 L7 7 L8.8 8 L8 9 Q5 8.6 3 4 Z" fill="#fff"/></svg>
        012-345-6789
      </li>
      <li>
        <svg class="contact-icon" viewBox="0 0 12 12" aria-hidden="true"><rect x="1" y="3" width="10" height="7" fill="#fff"/><path d="M1 3 L6 7 L11 3" fill="none" stroke="var(--brand-blue)" stroke-width="1"/></svg>
        name@kestrelhire.com.au
      </li>
      <li>
        <svg class="contact-icon" viewBox="0 0 12 12" aria-hidden="true"><circle cx="6" cy="6" r="5.5" fill="#fff"/><path d="M0.5 6 H11.5 M6 0.5 V11.5 M6 0.5 Q2.5 6 6 11.5 M6 0.5 Q9.5 6 6 11.5" fill="none" stroke="var(--brand-blue)" stroke-width="0.8"/></svg>
        www.kestrelhire.com.au
      </li>
    </ul>
  </section>

  <section class="card card-back" aria-label="Card back">
    <h2 class="brand-name">Kestrel Hire</h2>
  </section>
</main>
</body>
</html>
```